Business card - mobile service

O KiraVox is a mobile family safety service based on tablets and smartphones.
The business card must have:
BASIC INFO
Company Logo
Name
Position / Job Title: Co-founder
Mobile Phone Number: +55 (11) 5830 9172
Land Line: +55 (11) 8761 203945
Email Address: name@kiravox-example.com
Web Site URL: www.kiravox-example.com
PROMOTIONAL INFO
Try KiraVox free Today!
Your personal promo code: qqqq-5839-wwww-4162-9087
Promo code text explanation with the instructions about the trial offer
Updates
Dears,
One more must have: the KiraVox slogan:
Safety

```html
<!DOCTYPE html>
<html lang="en">
<head>
<meta charset="utf-8">
<title>KiraVox business card</title>
<link rel="stylesheet" href="https://fonts.googleapis.com/css2?family=Open+Sans:ital,wght@0,400;0,600;0,800;1,400&display=swap">
<style>
  :root {
    --bg: #e9e9ea;
    --brand-blue: #1ea3e3;
    --brand-blue-dark: #0f8ccc;
    --brand-yellow: #f6c31b;
    --ink: #1d1d1d;
    --divider: #6f6f6f;
    --card-white: #ffffff;
    --soft-white: rgba(255,255,255,.85);
  }
  * { box-sizing: border-box; margin: 0; padding: 0; }
  html, body { width: 1200px; height: 944px; overflow: hidden; }
  body {
    background: var(--bg);
    font-family: "Open Sans", Arial, sans-serif;
    position: relative;
  }
  .card {
    position: absolute;
    width: 640px;
    height: 366px;
    border-radius: 26px;
    box-shadow: 0 10px 28px rgba(0,0,0,.22);
    overflow: hidden;
  }
  /* front */
  .card-front {
    left: 70px; top: 80px;
    background: linear-gradient(160deg, var(--brand-blue) 0%, var(--brand-blue-dark) 100%);
    text-align: center;
  }
  .front-logo {
    margin: 46px auto 0;
    display: flex; align-items: center; justify-content: center; gap: 18px;
  }
  .front-logo .wordmark {
    font-weight: 800; font-size: 76px; line-height: 1; color: #fff;
    letter-spacing: -1px;
  }
  .logo-dot { width: 38px; height: 38px; border-radius: 50%; background: var(--brand-yellow); }
  .slogan { margin-top: 30px; color: #fff; font-size: 20px; line-height: 1.3; }
  .promo-line {
    margin-top: 6px; color: var(--brand-yellow);
    font-size: 22px; line-height: 1.3; text-transform: uppercase; letter-spacing: .5px;
  }
  .promo-code {
    margin-top: 14px; color: #fff; font-size: 16px; line-height: 1.3;
  }
  .promo-code strong { font-weight: 600; letter-spacing: .5px; }
  .promo-note {
    margin: 6px auto 0; width: 470px; color: var(--soft-white);
    font-size: 13px; line-height: 1.4;
  }
  /* back */
  .card-back {
    left: 490px; top: 480px;
    background: var(--card-white);
    display: flex; align-items: center;
  }
  .back-brand {
    width: 290px; display: flex; flex-direction: column; align-items: center; gap: 6px;
  }
  .back-logo { display: flex; align-items: center; gap: 12px; }
  .back-logo .wordmark {
    font-weight: 800; font-size: 56px; line-height: 1.1; color: var(--brand-blue); letter-spacing: -1px;
  }
  .back-logo .logo-dot { width: 28px; height: 28px; }
  .back-tagline {
    color: var(--brand-yellow); font-weight: 600; font-size: 18px;
    text-transform: uppercase; letter-spacing: 4px;
  }
  .divider { width: 2px; height: 196px; background: var(--divider); }
  .contact { padding-left: 24px; color: var(--ink); font-size: 17px; line-height: 1.3; }
  .contact .name { color: var(--brand-blue); font-size: 23px; }
  .contact .role { font-style: italic; font-size: 17px; margin-bottom: 26px; }
  .contact .label { color: var(--brand-blue); }
  .contact .web { color: var(--brand-blue); }
</style>
</head>
<body>
  <section class="card card-front" aria-label="Card front">
    <div class="front-logo">
      <span class="wordmark">KiraVox</span>
      <span class="logo-dot" aria-hidden="true"></span>
    </div>
    <p class="slogan">Your Family Safety Service</p>
    <p class="promo-line">Try KiraVox free Today!</p>
    <p class="promo-code">Your personal promo code: <strong>qqqq-5839-wwww-4162-9087</strong></p>
    <p class="promo-note">Sign up at www.kiravox-example.com and enter this code to start your free trial on any tablet or smartphone.</p>
  </section>

  <section class="card card-back" aria-label="Card back">
    <div class="back-brand">
      <div class="back-logo">
        <span class="wordmark">KiraVox</span>
        <span class="logo-dot" aria-hidden="true"></span>
      </div>
      <p class="back-tagline">Safety</p>
    </div>
    <div class="divider"></div>
    <div class="contact">
      <p class="name">Theo Marlund</p>
      <p class="role">Co-founder</p>
      <p><span class="label">Mobile:</span> +55 (11) 5830 9172</p>
      <p><span class="label">Phone:</span> +55 (11) 8761 203945</p>
      <p><span class="label">Email:</span> theo@kiravox-example.com</p>
      <p class="web">www.kiravox-example.com</p>
    </div>
  </section>
</body>
</html>
```